Design a Book Cover for a Bill Tracker Logbook

We are looking for a designer to create a book cover for a bill tracker. The detailed instructions and interior pages are attached. For those who are new to BVN, the cover template is also attached.
Please be creative and focus on creating a trustworthy, reliable, modern, and secure feeling based on the theme. You are allowed to use downloaded templates, but you must provide commercial licenses.
Attention: We are happy to pay extra tip if you are selected with a really high quality design.
Target Market(s)
US

```html
<!DOCTYPE html>
<html lang="en">
<head>
<meta charset="utf-8">
<title>Bill Tracker &amp; Password Log – Cover</title>
<link href="https://fonts.googleapis.com/css2?family=Playfair+Display:wght@400&family=Source+Sans+3:ital,wght@0,400;0,600;1,400;1,600&display=swap" rel="stylesheet">
<style>
  :root {
    --cover-blue: #0155aa;
    --ghost-blue: #1c62b4;
    --rule-blue: #6f9fd6;
    --paper: #ffffff;
    --paper-line: #9aa3ad;
    --paper-shade: #dfe4ea;
    --ink-white: #ffffff;
  }
  html, body {
    margin: 0;
    padding: 0;
    overflow: hidden;
  }
  .cover {
    position: relative;
    width: 1200px;
    height: 772px;
    background: var(--cover-blue);
    overflow: hidden;
    color: var(--ink-white);
    font-family: "Source Sans 3", sans-serif;
  }
  /* Back cover */
  .back-note {
    position: absolute;
    left: 148px;
    top: 126px;
    width: 300px;
    margin: 0;
    text-align: center;
    font-size: 9.6px;
    line-height: 13.4px;
  }
  .publisher {
    position: absolute;
    left: 238px;
    top: 473px;
    width: 120px;
    display: flex;
    flex-direction: column;
    align-items: center;
    gap: 4px;
  }
  .publisher-dot {
    width: 40px;
    height: 40px;
    border-radius: 50%;
    background: #1c2b3f;
    border: 2px solid #c9d3de;
    box-sizing: border-box;
  }
  .publisher-name {
    font-size: 8px;
    font-weight: 600;
    letter-spacing: 0.5px;
  }
  /* Spine */
  .spine-title {
    position: absolute;
    left: 592px;
    top: 96px;
    writing-mode: vertical-rl;
    font-family: "Playfair Display", serif;
    font-size: 10.5px;
    letter-spacing: 1.3px;
    white-space: nowrap;
  }
  /* Front cover */
  .ghost-word {
    position: absolute;
    margin: 0;
    color: var(--ghost-blue);
    font-size: 64px;
    font-weight: 600;
    font-style: italic;
    line-height: 1;
    white-space: nowrap;
  }
  .ghost-contacts { left: 704px; top: 322px; }
  .ghost-password { left: 824px; top: 420px; }
  .ghost-bill { left: 824px; top: 526px; }

  .title {
    margin: 0;
    font-weight: 400;
  }
  .title-line {
    position: absolute;
    left: 600px;
    width: 596px;
    text-align: center;
    font-family: "Playfair Display", serif;
    font-size: 56px;
    line-height: 1;
    letter-spacing: -2px;
    white-space: nowrap;
  }
  .title-top { top: 96px; }
  .title-bottom { top: 192px; }
  .title-join {
    position: absolute;
    left: 600px;
    width: 596px;
    top: 154px;
    text-align: center;
    font-family: "Source Sans 3", sans-serif;
    font-size: 48px;
    line-height: 48px;
  }
  .title-rule {
    position: absolute;
    top: 172px;
    height: 2px;
    background: var(--rule-blue);
  }
  .title-rule-left { left: 730px; width: 142px; }
  .title-rule-right { left: 924px; width: 146px; }

  .date-range {
    position: absolute;
    left: 694px;
    top: 271px;
    width: 400px;
    margin: 0;
    text-align: center;
    font-size: 15px;
    word-spacing: 3px;
  }
  .tagline {
    position: absolute;
    margin: 0;
    font-style: italic;
    font-size: 11.5px;
    white-space: nowrap;
  }
  .tagline-contacts { left: 832px; top: 382px; }
  .tagline-payments { left: 834px; top: 588px; }

  .page-preview {
    position: absolute;
    left: 644px;
    top: 412px;
    width: 166px;
    height: 188px;
  }
  .page-count {
    position: absolute;
    left: 760px;
    top: 660px;
    width: 290px;
    margin: 0;
    text-align: center;
    font-size: 28px;
    letter-spacing: -0.5px;
  }
  .page-count strong {
    font-weight: 400;
    font-size: 36px;
  }
</style>
</head>
<body>
<main class="cover">
  <!-- Back cover -->
  <p class="back-note">
    Thank you for choosing ‘Bill Tracker &amp; Password Log’.<br>
    Please leave a review on Shelfwise if you find it helpful in your Life.<br>
    This will help us to produce more high quality content.<br>
    Thank You
  </p>
  <div class="publisher">
    <span class="publisher-dot"></span>
    <span class="publisher-name">LUMEN PRESS</span>
  </div>

  <!-- Spine -->
  <div class="spine-title">BILL TRACKER &amp; PASSWORD LOG</div>

  <!-- Front cover -->
  <p class="ghost-word ghost-contacts" aria-hidden="true">Contacts</p>
  <p class="ghost-word ghost-password" aria-hidden="true">Password Log</p>
  <p class="ghost-word ghost-bill" aria-hidden="true">Bill Tracker</p>

  <h1 class="title">
    <span class="title-line title-top">BILL TRACKER</span>
    <span class="title-rule title-rule-left"></span>
    <span class="title-join">&amp;</span>
    <span class="title-rule title-rule-right"></span>
    <span class="title-line title-bottom">PASSWORD LOG</span>
  </h1>

  <p class="date-range">FROM 20__ to 20__</p>

  <p class="tagline tagline-contacts">Save Passwords and Contacts</p>

  <svg class="page-preview" viewBox="0 0 166 188" role="img" aria-label="Fanned sample interior pages: contacts sheet, password log sheet and bill tracker table">
    <rect x="0" y="0" width="166" height="188" rx="2" fill="var(--paper-shade)"/>
  </svg>

  <p class="tagline tagline-payments">Track Payments up to 8 Years</p>

  <p class="page-count">over <strong>100</strong> pages</p>
</main>
</body>
</html>
```